Bref créative
Bridgewell Brochure
Brochure
The brochure I want is a double-sided, tri-fold, 8.5" x 11". I have uploaded a sketch on what I would like on each side, as well as my original brochure. I will describe what I want on each side, and each section.
Inside (refer to formatting of original brochure):
left -- I want this section to be very similar to the original, but with a new design consistent with our colors and logo. Attached is a file titled "Bridgewell Brochure -- NEW TEXT" that is the new text I want in the section.
middle -- I want the text of the original brochure to remain the same, but consistent with new design/colors, and also if we can use our logo's "cube" as the new separator between the testimonials.
right -- I want this to be all new (not like original), with the text, "Visit us on the web at: www.BridgewellHoldingsNY.example" and below that, the text, "find our Attorney tab". The designer is open to design this section any way they would like, consistent with the overall design.
Outside (refer to formatting of original brochure):
left -- this section can be just like the original brochure, just with the updated design. I still want 'scales of justice' included in this section.
middle -- same as original brochure, just with our new address: 418 Maplecrest Avenue, Floral Park, NY 11001
right -- same as original brochure, just with new design
On the whole, I am looking for a design that is a little more sleek, modern, and simple. I would urge the designers to please stay away from swirly text or design features.
Real Estate
attorneys and businessmen
I have uploaded both sides of our old brochure. We want something nearly identical, just more reflective of our colors and style.
I have also uploaded our logo, business card, and new text for the left side of the inside of the brochure.
Lastly, I am uploading a new mock-up of the 6 sections of the brochure (similar to old version).
ANY SUBMISSION THAT DEVIATES TOO MUCH FROM OUR PREVIOUS DESIGN WILL BE IMMEDIATELY ELIMINATED.

```html
<!DOCTYPE html>
<html lang="en">
<head>
<meta charset="utf-8">
<title>Bridgewell Asset Management – Tri-fold Brochure</title>
<link rel="stylesheet" href="https://fonts.googleapis.com/css2?family=Archivo+Narrow:wght@400;700&family=Tinos:ital,wght@0,400;0,700;1,400&display=swap">
<style>
  :root {
    --purple: #2f2a6b;
    --purple-deep: #221e55;
    --gold: #e29a16;
    --gold-soft: #f0b347;
    --paper: #ffffff;
    --ink: #2b2b2b;
    --stage: #ecebe6;
    --cube-light: #f4f2ec;
    --cube-shade: #d9d6cc;
  }
  * { box-sizing: border-box; margin: 0; padding: 0; }
  html, body { width: 1200px; height: 901px; overflow: hidden; }
  body {
    background: var(--stage);
    font-family: "Tinos", "Times New Roman", serif;
    color: var(--ink);
    position: relative;
  }
  .spread {
    position: absolute;
    left: 320px;
    width: 560px;
    height: 433px;
    background: var(--paper);
    display: grid;
    grid-template-columns: repeat(3, 1fr);
    box-shadow: 0 2px 8px rgba(0,0,0,.18);
  }
  .spread--outside { top: 12px; }
  .spread--inside { top: 456px; }
  .panel { position: relative; padding: 16px 14px; overflow: hidden; }

  /* Outside – offering panel */
  .offering-title {
    display: inline-block;
    background: var(--gold);
    color: var(--paper);
    font-family: "Archivo Narrow", Arial, sans-serif;
    font-weight: 700;
    font-size: 17px;
    letter-spacing: .5px;
    padding: 3px 26px 3px 8px;
    margin-bottom: 8px;
  }
  .offering-list { list-style: none; }
  .offering-list li {
    color: var(--gold);
    font-size: 11.5px;
    margin-bottom: 6px;
    padding-left: 10px;
    position: relative;
  }
  .offering-list li::before {
    content: ""; position: absolute; left: 0; top: 5px;
    width: 4px; height: 4px; background: var(--gold);
  }
  .scales-art {
    position: absolute; left: 20px; top: 170px;
    width: 96px; height: 86px;
    background: linear-gradient(160deg, var(--purple), var(--purple-deep));
    opacity: .9;
  }
  .tollfree {
    position: absolute; left: 14px; bottom: 34px;
    font-size: 10px; color: var(--gold); font-style: italic;
  }
  .phone {
    position: absolute; left: 14px; bottom: 12px;
    font-family: "Archivo Narrow", Arial, sans-serif;
    font-size: 21px; color: var(--purple-deep);
  }

  /* Outside – mailing panel */
  .return-address {
    position: absolute; left: 18px; top: 14px;
    writing-mode: vertical-rl;
    font-size: 8px; line-height: 1.35; color: var(--purple);
  }
  .cube-art {
    position: absolute;
    background: linear-gradient(135deg, var(--cube-light) 0%, var(--cube-light) 55%, var(--cube-shade) 100%);
  }
  .spread--outside .cube-art { left: 10px; right: 0; top: 150px; bottom: 14px; }

  /* Outside – cover panel */
  .cover-band {
    position: absolute; left: 0; top: 0; bottom: 0; width: 40px;
    background: var(--purple);
  }
  .cover-headline {
    position: absolute; left: 50px; top: 24px; right: 8px;
    font-family: "Archivo Narrow", Arial, sans-serif;
    font-weight: 700; font-size: 24px; line-height: 1.02;
    color: var(--gold);
  }
  .brand {
    position: absolute; left: 60px; bottom: 20px; right: 8px;
    display: flex; flex-direction: column; align-items: center; gap: 5px;
  }
  .brand-mark { width: 16px; height: 16px; background: var(--purple); }
  .brand-name {
    font-family: "Archivo Narrow", Arial, sans-serif;
    font-weight: 700; font-size: 12px; line-height: 1.05;
    color: var(--purple); text-align: center; letter-spacing: .3px;
  }

  /* Inside */
  .section-head {
    background: var(--purple);
    color: var(--gold-soft);
    font-family: "Archivo Narrow", Arial, sans-serif;
    font-weight: 700; font-size: 10.5px; letter-spacing: .3px;
    padding: 4px 7px; margin-bottom: 7px;
  }
  .body-copy { font-size: 7.6px; line-height: 1.35; margin-bottom: 7px; text-align: justify; }
  .body-copy strong { color: var(--purple); }
  .lead-in { font-style: italic; font-size: 9.5px; margin-bottom: 8px; }
  .testimonial { font-size: 7.4px; line-height: 1.35; text-align: center; }
  .testimonial-name { display: block; margin-top: 4px; font-style: italic; }
  .separator { width: 13px; height: 13px; background: var(--purple); margin: 8px auto; }
  .web-head {
    font-family: "Archivo Narrow", Arial, sans-serif;
    font-weight: 700; font-size: 10.5px; color: var(--purple);
  }
  .web-url {
    font-family: "Archivo Narrow", Arial, sans-serif;
    font-weight: 700; font-size: 9.5px; color: var(--gold); word-break: break-all;
  }
  .web-note { font-size: 8px; font-style: italic; color: var(--purple); margin-top: 2px; }
  .spread--inside .cube-art { left: 0; right: 0; top: 150px; bottom: 14px; }
</style>
</head>
<body>

<section class="spread spread--outside">
  <div class="panel panel--offering">
    <div class="offering-title">OFFERING</div>
    <ul class="offering-list">
      <li>Prompt Professional Services</li>
      <li>Seamless Closings</li>
      <li>All Cash Purchases</li>
      <li>Honesty &amp; Integrity</li>
    </ul>
    <div class="scales-art" role="img" aria-label="Scales of justice illustration"></div>
    <div class="tollfree">Toll Free</div>
    <div class="phone">1-800-555-0147</div>
  </div>

  <div class="panel panel--mailing">
    <div class="return-address">Bridgewell Asset Management<br>418 Maplecrest Avenue<br>Floral Park, NY 11001</div>
    <div class="cube-art" role="img" aria-label="Large pale three-dimensional cube illustration"></div>
  </div>

  <div class="panel panel--cover">
    <div class="cover-band"></div>
    <h1 class="cover-headline">PROVIDING SOLUTIONS FOR YOU &amp; YOUR CLIENTS!</h1>
    <div class="brand">
      <span class="brand-mark"></span>
      <span class="brand-name">BRIDGEWELL<br>ASSET MANAGEMENT</span>
    </div>
  </div>
</section>

<section class="spread spread--inside">
  <div class="panel panel--about">
    <h2 class="section-head">DRIVEN BY RESULTS</h2>
    <p class="body-copy">Bridgewell Asset Management has established itself as a premier investment corporation specializing in the purchase of properties in distressed conditions or facing sale due to estate or foreclosure.</p>
    <p class="body-copy">We recognize this is a complex situation, where sellers rely on trusted partners. With extensive experience in real estate financing, title and settlement, we are able to provide dependable resources for professionals and their clients.</p>
    <h2 class="section-head">WHEN A CLOSING IS NEEDED</h2>
    <p class="body-copy">Bridgewell closes through an all-cash offer, so our purchases are not subject to mortgage contingencies. <strong>Reliability</strong> is one of our greatest assets.</p>
    <p class="body-copy"><strong>Bridgewell Asset Management</strong> looks forward to the opportunity to provide outstanding service to you and your clients.</p>
  </div>

  <div class="panel panel--testimonials">
    <h2 class="section-head">DON'T JUST TAKE OUR WORD FOR IT</h2>
    <p class="lead-in">Hear what your colleagues have to say!</p>
    <p class="testimonial">"I have had the pleasure of dealing with the principal officers on numerous occasions. In each instance they have kept their word and closed deals timely. I rely on them without a second thought."<span class="testimonial-name">Karen L. Ostrava<br>Attorney at Law</span></p>
    <div class="separator"></div>
    <p class="testimonial">"I have been very satisfied in the way they conduct their business. Their fresh, direct approach delivers real results, and our clients feel respected."<span class="testimonial-name">Melissa Danbury<br>Attorney at Law</span></p>
    <div class="separator"></div>
    <p class="testimonial">"Bridgewell is diligent and professional. They settle in a timely, honest fashion and make the whole transaction a pleasure to work with."<span class="testimonial-name">Ben Harlow<br>Attorney at Law</span></p>
  </div>

  <div class="panel panel--web">
    <p class="web-head">VISIT US ON THE WEB AT:</p>
    <p class="web-url">www.BridgewellHoldingsNY.example</p>
    <p class="web-note">(find our Attorney tab)</p>
    <div class="cube-art" role="img" aria-label="Large pale three-dimensional cube illustration"></div>
  </div>
</section>

</body>
</html>
```